Lumora Digital - Layout Design

We need a web design for a new company based in Australia, called "Lumora Digital". We develop innovative custom web applications for Out Of Home, and Media companies.
Our initial website is a one page type of site. I've created a simple wireframe to show you what we need: https://sketchplot.example/k3Tq9W
Here is a layout reference: http://folvex.example/
( note - the designs needs to follow our branding guidelines (attached).
The top feature could be just solid color or an abstract subtle pattern or illustration that conveys the specialization of our business in the area of out of home, map, data.
In the attachment you will also find some images added for the work section.
Updates
Target Market(s)
Media and Advertising
Industry/Entity Type
Digital
Number of Pages Required
1 page
Look and feel
Each slider illustrates characteristics of the customer's brand and the style your logo design should communicate.

```html
<!DOCTYPE html>
<html lang="en">
<head>
<meta charset="utf-8">
<title>Lumora Digital</title>
<link rel="stylesheet" href="https://fonts.googleapis.com/css2?family=Lato:ital,wght@0,300;0,400;0,700;0,900;1,400&family=Courgette&display=swap">
<style>
:root{
  --red:#f0443f;
  --red-dark:#d93530;
  --ink:#2b2f36;
  --text:#6a6e74;
  --muted:#9a9ea4;
  --light:#f3f3f3;
  --lighter:#f8f8f8;
  --navy:#1c2630;
  --white:#ffffff;
}
*{box-sizing:border-box;margin:0;padding:0}
html,body{width:1200px;height:4580px;overflow:hidden}
body{font-family:"Lato",sans-serif;color:var(--text);background:var(--white);font-size:12px;line-height:1.6}
.nav{height:68px;display:flex;align-items:center;justify-content:space-between;padding:0 165px 0 170px;background:var(--white)}
.brand{display:flex;align-items:center;gap:8px;font-weight:700;font-size:22px;color:var(--ink)}
.brand-dot{width:10px;height:10px;background:var(--red);border-radius:50%}
.nav-links{display:flex;gap:30px;list-style:none;font-size:13px;color:var(--ink)}
.hero{height:504px;background:var(--red);position:relative;color:var(--white);padding:92px 0 0 170px}
.hero h1{font-weight:900;font-size:48px;line-height:1.05;letter-spacing:.5px;text-transform:uppercase;width:460px}
.hero p{margin-top:20px;width:390px;font-size:13px;line-height:1.55;color:#ffe6e4}
.btn{display:inline-block;margin-top:26px;background:var(--navy);color:var(--white);font-weight:700;font-size:12px;padding:10px 20px;letter-spacing:.5px}
.hero-screen{position:absolute;left:660px;top:96px;width:360px;height:250px;background:var(--white);border-radius:6px;box-shadow:0 10px 30px rgba(0,0,0,.25);padding:14px}
.hero-screen .fill{width:100%;height:100%;background:linear-gradient(135deg,#3fc3e0,#2a5fb8 45%,#e34a8c 80%,#f5c542)}
.dots{position:absolute;left:0;right:0;bottom:34px;display:flex;justify-content:center;gap:6px}
.dots span{width:9px;height:9px;background:var(--white);border-radius:2px;opacity:.9}
.section-title{text-align:center;font-weight:300;font-size:40px;color:var(--ink);line-height:1.2}
.rule{width:60px;height:2px;background:var(--red);margin:14px auto 0}
.about{height:248px;padding-top:36px}
.lead{width:720px;margin:32px auto 0;text-align:center;font-size:12px}
.team{height:920px;background:var(--light);padding-top:50px}
.board{height:820px;background:var(--lighter);padding-top:50px;border-top:1px solid #e6e6e6}
.person{text-align:center;margin-top:30px}
.photo{width:100px;height:100px;border-radius:50%;margin:0 auto;background:linear-gradient(160deg,#c9b8a8,#7a6a5e)}
.person h3{margin-top:14px;font-size:13px;font-weight:700;color:var(--ink)}
.person p{width:400px;margin:8px auto 0;font-size:11px;line-height:1.55}
.services{height:320px;padding-top:40px}
.service-cols{display:flex;justify-content:space-between;width:860px;margin:40px auto 0}
.service{width:250px}
.service h4{color:var(--red);font-size:12px;font-weight:700;text-transform:uppercase;margin-bottom:8px}
.service p{font-size:11px;line-height:1.55}
.exp-head{height:140px;padding-top:40px;border-top:1px solid #e6e6e6}
.project{height:290px;display:flex;align-items:center;gap:40px;padding:0 170px}
.project.alt{background:var(--light)}
.shot{width:430px;height:230px;flex:none;box-shadow:0 4px 14px rgba(0,0,0,.18)}
.shot.outdoor{background:linear-gradient(135deg,#40c4e2,#2d62ba 45%,#e44a8d 80%,#f4c443)}
.shot.search{background:linear-gradient(180deg,#2d3640,#5b6a78)}
.shot.media{background:linear-gradient(120deg,#1a1a1a,#4a6f8a 60%,#c9d3dc)}
.shot.radio{background:linear-gradient(180deg,#f06b2b,#2a2a2a 30%,#3d3d3d)}
.info{flex:1}
.project.alt .info{text-align:right}
.info h3{color:var(--red);font-size:15px;font-weight:700}
.info p{font-size:11px;line-height:1.55;margin-top:8px}
.meta{display:flex;align-items:center;gap:8px;margin-top:14px;font-size:11px;color:var(--ink)}
.project.alt .meta{justify-content:flex-end}
.meta svg{display:block}
.link{display:flex;align-items:center;gap:8px;margin-top:8px;font-size:11px;color:var(--red)}
.project.alt .link{justify-content:flex-end}
.contact{height:400px;background:var(--navy);color:#c4cad0;text-align:center;padding-top:56px}
.contact h2{color:var(--white);font-weight:400;font-size:24px;letter-spacing:1px}
.tagline{font-family:"Courgette",cursive;color:var(--red);font-size:24px;line-height:1.4;margin-top:34px}
.address{margin-top:24px;font-size:12px}
.contact-lines{display:flex;justify-content:center;gap:60px;margin-top:24px;font-size:12px}
.contact-lines span{display:flex;align-items:center;gap:8px}
.socials{display:flex;justify-content:center;gap:10px;margin-top:22px}
.socials span{width:16px;height:16px;border-radius:50%;background:var(--red)}
</style>
</head>
<body>
<header class="nav">
  <div class="brand"><span class="brand-dot"></span>Lumora Digital</div>
  <ul class="nav-links"><li>About</li><li>Team</li><li>Services</li><li>Experience</li><li>Contact</li></ul>
</header>

<section class="hero">
  <h1>Lorem ipsum dolor sit amet</h1>
  <p>This is a sample hero statement. Lorem ipsum dolor sit amet, consectetur adipiscing elit, sed do eiusmod tempor incididunt ut labore et dolore magna aliqua.</p>
  <span class="btn">LEARN MORE</span>
  <div class="hero-screen"><div class="fill" role="img" aria-label="Laptop screen showing a colourful outdoor advertising web application"></div></div>
  <div class="dots"><span></span><span></span><span></span></div>
</section>

<section class="about">
  <h2 class="section-title">About Us</h2>
  <div class="rule"></div>
  <p class="lead">We are Lumora Digital, a team of innovators, thinkers and doers providing data-driven web applications for out of home and media companies. With decades of experience between us across a variety of sectors, Lumora Digital is a business focused on helping organisations grow more value from information, through insight and action.</p>
</section>

<section class="team">
  <h2 class="section-title">Key Team</h2>
  <div class="rule"></div>
  <p class="lead">Sed ut perspiciatis unde omnis iste natus error sit voluptatem accusantium doloremque laudantium, totam rem aperiam, eaque ipsa quae ab illo inventore veritatis et quasi architecto beatae vitae dicta sunt explicabo.</p>
  <div class="person"><div class="photo" role="img" aria-label="Portrait photo of Clara Wendell"></div><h3>Clara Wendell - CEO</h3><p>Sed ut perspiciatis unde omnis iste natus error sit voluptatem accusantium doloremque laudantium, totam rem aperiam, eaque ipsa quae ab illo inventore veritatis et quasi architecto beatae vitae dicta sunt explicabo.</p></div>
  <div class="person"><div class="photo" role="img" aria-label="Portrait photo of Owen Hartley"></div><h3>Owen Hartley - CTO</h3><p>Sed ut perspiciatis unde omnis iste natus error sit voluptatem accusantium doloremque laudantium, totam rem aperiam, eaque ipsa quae ab illo inventore veritatis et quasi architecto beatae vitae dicta sunt explicabo.</p></div>
  <div class="person"><div class="photo" role="img" aria-label="Portrait photo of Felix Marlow"></div><h3>Felix Marlow - Executive Partner</h3><p>Sed ut perspiciatis unde omnis iste natus error sit voluptatem accusantium doloremque laudantium, totam rem aperiam, eaque ipsa quae ab illo inventore veritatis et quasi architecto beatae vitae dicta sunt explicabo.</p></div>
</section>

<section class="board">
  <h2 class="section-title">Board Of Advisors</h2>
  <div class="rule"></div>
  <p class="lead">Sed ut perspiciatis unde omnis iste natus error sit voluptatem accusantium doloremque laudantium, totam rem aperiam, eaque ipsa quae ab illo inventore veritatis et quasi architecto beatae vitae dicta sunt explicabo.</p>
  <div class="person"><div class="photo" role="img" aria-label="Portrait photo of Nadia Brooks"></div><h3>Nadia Brooks</h3><p>Sed ut perspiciatis unde omnis iste natus error sit voluptatem accusantium doloremque laudantium, totam rem aperiam, eaque ipsa quae ab illo inventore veritatis et quasi architecto beatae vitae dicta sunt explicabo.</p></div>
  <div class="person"><div class="photo" role="img" aria-label="Portrait photo of Clara Wendell"></div><h3>Clara Wendell</h3><p>Sed ut perspiciatis unde omnis iste natus error sit voluptatem accusantium doloremque laudantium, totam rem aperiam, eaque ipsa quae ab illo inventore veritatis et quasi architecto beatae vitae dicta sunt explicabo.</p></div>
</section>

<section class="services">
  <h2 class="section-title">Services</h2>
  <div class="rule"></div>
  <div class="service-cols">
    <div class="service"><h4>Lorem ipsum ss</h4><p>Sed ut perspiciatis unde omnis iste natus error sit voluptatem accusantium doloremque laudantium, totam rem aperiam, eaque ipsa quae ab illo inventore veritatis et quasi architecto beatae vitae dicta sunt explicabo.</p></div>
    <div class="service"><h4>Lorem ipsum ss</h4><p>Sed ut perspiciatis unde omnis iste natus error sit voluptatem accusantium doloremque laudantium, totam rem aperiam, eaque ipsa quae ab illo inventore veritatis et quasi architecto beatae vitae dicta sunt explicabo.</p></div>
    <div class="service"><h4>Lorem ipsum ss</h4><p>Sed ut perspiciatis unde omnis iste natus error sit voluptatem accusantium doloremque laudantium, totam rem aperiam, eaque ipsa quae ab illo inventore veritatis et quasi architecto beatae vitae dicta sunt explicabo.</p></div>
  </div>
</section>

<section class="exp-head">
  <h2 class="section-title">Experience</h2>
  <div class="rule"></div>
</section>

<article class="project">
  <div class="shot outdoor" role="img" aria-label="Screenshot of the Arcline Outdoor web application"></div>
  <div class="info">
    <h3>Arcline Outdoor</h3>
    <p>Sed ut perspiciatis unde omnis iste natus error sit voluptatem accusantium doloremque laudantium, totam rem aperiam, eaque ipsa quae ab illo inventore veritatis et quasi architecto.</p>
    <div class="meta">Platforms:
      <svg width="20" height="14" viewBox="0 0 20 14"><rect x="1" y="1" width="18" height="10" fill="none" stroke="#2b2f36" stroke-width="1.5"/><path d="M6 13h8" stroke="#2b2f36" stroke-width="1.5"/></svg>
      <svg width="10" height="14" viewBox="0 0 10 14"><rect x="1" y="1" width="8" height="12" rx="1" fill="none" stroke="#2b2f36" stroke-width="1.5"/></svg>
      <svg width="14" height="14" viewBox="0 0 14 14"><rect x="1" y="1" width="12" height="12" rx="1" fill="none" stroke="#2b2f36" stroke-width="1.5"/></svg>
    </div>
    <div class="link"><svg width="12" height="12" viewBox="0 0 12 12"><circle cx="6" cy="6" r="5" fill="none" stroke="#f0443f" stroke-width="1.5"/></svg>www.arclineoutdoor.example</div>
  </div>
</article>

<article class="project alt">
  <div class="info">
    <h3>Pivra - Local Search Engine</h3>
    <p>Sed ut perspiciatis unde omnis iste natus error sit voluptatem accusantium doloremque laudantium, totam rem aperiam, eaque ipsa quae ab illo inventore veritatis et quasi architecto.</p>
    <div class="meta">
      <svg width="20" height="14" viewBox="0 0 20 14"><rect x="1" y="1" width="18" height="10" fill="none" stroke="#2b2f36" stroke-width="1.5"/><path d="M6 13h8" stroke="#2b2f36" stroke-width="1.5"/></svg>
      <svg width="10" height="14" viewBox="0 0 10 14"><rect x="1" y="1" width="8" height="12" rx="1" fill="none" stroke="#2b2f36" stroke-width="1.5"/></svg>
      : Platforms</div>
    <div class="link">www.pivra.example<svg width="12" height="12" viewBox="0 0 12 12"><circle cx="6" cy="6" r="5" fill="none" stroke="#f0443f" stroke-width="1.5"/></svg></div>
  </div>
  <div class="shot search" role="img" aria-label="Screenshot of the Pivra local search engine website"></div>
</article>

<article class="project">
  <div class="shot media" role="img" aria-label="Photo of a digital street billboard by Halo Media"></div>
  <div class="info">
    <h3>Halo Media</h3>
    <p>Sed ut perspiciatis unde omnis iste natus error sit voluptatem accusantium doloremque laudantium, totam rem aperiam, eaque ipsa quae ab illo inventore veritatis et quasi architecto.</p>
    <div class="meta">Platforms:
      <svg width="20" height="14" viewBox="0 0 20 14"><rect x="1" y="1" width="18" height="10" fill="none" stroke="#2b2f36" stroke-width="1.5"/><path d="M6 13h8" stroke="#2b2f36" stroke-width="1.5"/></svg>
      <svg width="10" height="14" viewBox="0 0 10 14"><rect x="1" y="1" width="8" height="12" rx="1" fill="none" stroke="#2b2f36" stroke-width="1.5"/></svg>
    </div>
    <div class="link"><svg width="12" height="12" viewBox="0 0 12 12"><circle cx="6" cy="6" r="5" fill="none" stroke="#f0443f" stroke-width="1.5"/></svg>www.halomedia.example</div>
  </div>
</article>

<article class="project alt">
  <div class="info">
    <h3>Tunewell.fm</h3>
    <p>Sed ut perspiciatis unde omnis iste natus error sit voluptatem accusantium doloremque laudantium, totam rem aperiam, eaque ipsa quae ab illo inventore veritatis et quasi architecto.</p>
    <div class="meta">
      <svg width="20" height="14" viewBox="0 0 20 14"><rect x="1" y="1" width="18" height="10" fill="none" stroke="#2b2f36" stroke-width="1.5"/><path d="M6 13h8" stroke="#2b2f36" stroke-width="1.5"/></svg>
      <svg width="10" height="14" viewBox="0 0 10 14"><rect x="1" y="1" width="8" height="12" rx="1" fill="none" stroke="#2b2f36" stroke-width="1.5"/></svg>
      : Platforms</div>
    <div class="link">www.tunewell.example<svg width="12" height="12" viewBox="0 0 12 12"><circle cx="6" cy="6" r="5" fill="none" stroke="#f0443f" stroke-width="1.5"/></svg></div>
  </div>
  <div class="shot radio" role="img" aria-label="Screenshot of the Tunewell.fm radio website"></div>
</article>

<footer class="contact">
  <h2>CONTACT</h2>
  <p class="tagline">Curious about what we can do to help your organization?<br>Then please get in touch.</p>
  <p class="address">Lumora Digital Pty Ltd &nbsp;|&nbsp; Level 4, 18 Harbour Lane &nbsp;|&nbsp; Sydney NSW 2000 &nbsp;|&nbsp; Australia</p>
  <div class="contact-lines">
    <span><svg width="14" height="12" viewBox="0 0 14 12"><rect x="1" y="1" width="12" height="10" fill="none" stroke="#f0443f" stroke-width="1.4"/><path d="M1 1l6 5 6-5" fill="none" stroke="#f0443f" stroke-width="1.4"/></svg>hello@lumoradigital.example</span>
    <span><svg width="12" height="14" viewBox="0 0 12 14"><rect x="2" y="1" width="8" height="12" rx="1.5" fill="none" stroke="#f0443f" stroke-width="1.4"/></svg>02 5550 1842</span>
  </div>
  <div class="socials"><span></span><span></span><span></span></div>
</footer>
</body>
</html>
```